Harbinvale Crest Inc Tank Lining Services

I would check out our website for an a quick understanding of what Blasting and Painting "is". www.harbinvalecrestinc.example

I need to Design "sales postcard" or "company postcard" that outlines the TANK LINING division of our company. (What is a "tank lining"? It is a coating applied to the interior of a Water Tank or "Water Tower". There are certifications and special equipment needed to provide these services that make it a unique market) This is a NEW service we are offing to our customers.

We want to include photo's of: Sand Blasting, Painting, and Welding on a Ground Storage Tank. (please see attached)

Bullet points to include:
-Critical Areas
-Tank Inspections
-Manway Installation
-Fire/Domestic Water

Please Note: a little says a lot in regards to regards to data crammed into "postcards". Our market is one that won't need to be "spoon" fed. I need potential clients to read the name and our contact info (obviously).

Target Market(s)

Building Owners

Industry/Entity Type

Construction

Font styles to use
Sans Serif

Colors
0054AA
0677BA
7BADD7
CADEEF
E8F1F8

Requirements
Must have
• Layered photos or pictures
Nice to have
• Cropped Layered photos are good
Should not have
• to much clutter

```html
<!DOCTYPE html>
<html lang="en">
<head>
<meta charset="utf-8">
<title>Harbinvale Crest Inc — Tank Lining</title>
<link rel="stylesheet" href="https://fonts.googleapis.com/css2?family=Montserrat:wght@400;600;800&family=Oswald:wght@500&display=swap">
<style>
  :root {
    --navy-deep: #17366f;
    --navy: #1f4a93;
    --brand-blue: #0054AA;
    --ring-blue: #0677BA;
    --sky: #7BADD7;
    --mist: #CADEEF;
    --white: #ffffff;
    --accent-yellow: #F4C842;
    --pill-text: #1b2f66;
  }
  html, body { margin: 0; padding: 0; overflow: hidden; background: var(--navy-deep); }
  .postcard {
    position: relative;
    width: 1200px;
    height: 655px;
    overflow: hidden;
    background: radial-gradient(ellipse at 75% 35%, #27539e 0%, var(--navy) 45%, var(--navy-deep) 100%);
    font-family: "Montserrat", sans-serif;
    color: var(--white);
  }
  .decor { position: absolute; inset: 0; }

  .brand {
    position: absolute; left: 27px; top: 28px;
    display: flex; align-items: center; gap: 10px;
    font-family: "Montserrat", sans-serif;
    font-weight: 600; font-size: 22px; color: var(--white);
  }
  .brand-square { width: 30px; height: 30px; border: 2.5px solid var(--white); box-sizing: border-box; }

  .photo {
    position: absolute; border-radius: 50%;
  }
  .photo-spraying {
    left: 0; top: 129px; width: 410px; height: 440px;
    border-radius: 50%;
    left: -5px; width: 420px; top: 129px; height: 444px;
    background: radial-gradient(circle at 40% 45%, #e6e6e3 0%, #9c968d 35%, #4a3f35 75%, #2b241e 100%);
  }
  .photo-inspection {
    left: 470px; top: 96px; width: 204px; height: 204px;
    background: radial-gradient(circle at 35% 30%, #f4f4f2 0%, #b6b6b2 40%, #7d7c79 100%);
  }
  .photo-welding {
    left: 461px; top: 409px; width: 290px; height: 290px;
    background: radial-gradient(circle at 50% 55%, #f5c9a0 0%, #d8323a 30%, #b01e29 70%, #3a2630 100%);
  }

  .headline { position: absolute; right: 52px; margin: 0; text-align: right; line-height: 1; }
  .headline-tank {
    top: 68px; font-weight: 800; font-size: 67px; letter-spacing: 1px;
  }
  .headline-lining {
    top: 138px; font-weight: 600; font-size: 104px; letter-spacing: 3px;
    color: transparent; -webkit-text-stroke: 2.5px var(--white);
  }

  .services-band {
    position: absolute; left: 745px; right: 0; top: 273px; height: 50px;
    background: var(--ring-blue); border-radius: 25px 0 0 25px;
  }
  .services-band::before {
    content: ""; position: absolute; left: 60px; right: 0; top: 24px; height: 2px; background: var(--white);
  }
  .service-pill {
    position: absolute; top: 9px; height: 33px; border-radius: 17px;
    background: var(--accent-yellow); color: var(--pill-text);
    font-family: "Oswald", sans-serif; font-weight: 500; font-size: 19px;
    display: flex; align-items: center; justify-content: center;
  }
  .pill-welding { left: 23px; width: 87px; }
  .pill-painting { left: 138px; width: 93px; }
  .pill-blasting { left: 256px; width: 147px; }

  .feature-list {
    position: absolute; right: 52px; top: 360px; margin: 0; padding: 0; list-style: none;
    text-align: right;
  }
  .feature-list li {
    font-size: 18.5px; font-weight: 400; letter-spacing: 1px; height: 42.5px; line-height: 28px;
    display: flex; justify-content: flex-end; align-items: center; gap: 14px; height: 28px; margin-bottom: 14.5px;
  }
  .feature-list li::after {
    content: ""; width: 0; height: 0;
    border-top: 8px solid transparent; border-bottom: 8px solid transparent;
    border-right: 14px solid var(--accent-yellow);
  }

  .social-row { position: absolute; right: 52px; top: 570px; display: flex; gap: 13px; }
  .social-dot { width: 26px; height: 26px; border: 2px solid var(--white); border-radius: 50%; }

  .website {
    position: absolute; right: 52px; top: 608px; font-size: 16px; font-weight: 600; letter-spacing: 1.6px;
  }
</style>
</head>
<body>
<main class="postcard">
  <svg class="decor" width="1200" height="655" viewBox="0 0 1200 655" aria-hidden="true">
    <!-- rings -->
    <circle cx="205" cy="350" r="242" fill="var(--ring-blue)"/>
    <circle cx="205" cy="350" r="226" fill="var(--white)"/>
    <circle cx="572" cy="198" r="123" fill="var(--ring-blue)"/>
    <circle cx="572" cy="198" r="112" fill="var(--white)"/>
    <circle cx="606" cy="554" r="173" fill="var(--ring-blue)"/>
    <circle cx="606" cy="554" r="159" fill="var(--white)"/>
    <!-- dot grids -->
    <g fill="var(--white)">
      <circle cx="460" cy="6" r="2.2"/><circle cx="473" cy="6" r="2.2"/><circle cx="486" cy="6" r="2.2"/><circle cx="499" cy="6" r="2.2"/><circle cx="512" cy="6" r="2.2"/><circle cx="525" cy="6" r="2.2"/>
      <circle cx="460" cy="19" r="2.2"/><circle cx="473" cy="19" r="2.2"/><circle cx="486" cy="19" r="2.2"/><circle cx="499" cy="19" r="2.2"/><circle cx="512" cy="19" r="2.2"/><circle cx="525" cy="19" r="2.2"/>
      <circle cx="1139" cy="18" r="2.6"/><circle cx="1152" cy="18" r="2.6"/><circle cx="1165" cy="18" r="2.6"/><circle cx="1178" cy="18" r="2.6"/><circle cx="1191" cy="18" r="2.6"/>
      <circle cx="1152" cy="29" r="2.6"/><circle cx="1165" cy="29" r="2.6"/><circle cx="1178" cy="29" r="2.6"/><circle cx="1191" cy="29" r="2.6"/>
      <circle cx="1165" cy="40" r="2.6"/><circle cx="1178" cy="40" r="2.6"/><circle cx="1191" cy="40" r="2.6"/>
      <circle cx="1178" cy="51" r="2.6"/><circle cx="1191" cy="51" r="2.6"/>
      <circle cx="1191" cy="63" r="2.6"/>
    </g>
    <!-- yellow accents -->
    <path d="M892 92 q8-14 22-8 q10 4 16-6 q8-10 16 0 q6 10-6 18 q-10 6-16 12 q-10 10-22 6 q-16-6-10-22z" fill="var(--accent-yellow)"/>
    <path d="M282 596 q12-16 30-14 q14 2 20-10 q8-14 22-4 q10 10-2 26 q-8 10-10 26 q-4 24-30 24 q-34-4-30-48z" fill="var(--accent-yellow)"/>
    <!-- corner stripes -->
    <g stroke="var(--white)" stroke-width="4" opacity="0.9">
      <line x1="0" y1="620" x2="10" y2="612"/><line x1="0" y1="634" x2="18" y2="618"/>
      <line x1="4" y1="645" x2="26" y2="625"/><line x1="14" y1="652" x2="33" y2="634"/>
      <line x1="26" y1="655" x2="38" y2="644"/>
    </g>
  </svg>

  <div class="brand">
    <span class="brand-square"></span>
    <span class="brand-name">Harbinvale Crest Inc</span>
  </div>

  <div class="photo photo-spraying" role="img" aria-label="Worker in protective suit and respirator spraying lining inside a tank"></div>
  <div class="photo photo-inspection" role="img" aria-label="Inspector checking a freshly coated tank interior with a flashlight"></div>
  <div class="photo photo-welding" role="img" aria-label="Welder working on the red interior wall of a storage tank"></div>

  <h1 class="headline headline-tank">TANK</h1>
  <h2 class="headline headline-lining">LINING</h2>

  <div class="services-band">
    <span class="service-pill pill-welding">WELDING</span>
    <span class="service-pill pill-painting">PAINTING</span>
    <span class="service-pill pill-blasting">SAND BLASTING</span>
  </div>

  <ul class="feature-list">
    <li>Critical Areas</li>
    <li>Tank Inspections</li>
    <li>Manway Installation</li>
    <li>Fire/Domestic Water</li>
  </ul>

  <div class="social-row" aria-hidden="true">
    <span class="social-dot"></span><span class="social-dot"></span><span class="social-dot"></span><span class="social-dot"></span>
  </div>

  <p class="website" style="margin:0">www.harbinvalecrestinc.example</p>
</main>
</body>
</html>
```